Flyer / Small Safety "Poster" (A4 or 8.5x11" paper)

We're looking to create a series of safety signs for woodworkers to print on home printers using standard sized paper (A4 or 8.5x11" depending on where they are), or possibly to have printed on 17x22" paper.
Currently we want only the first one, but keep in mind that all should work together.
They need: Simple graphic. Bold Text. Company logo. Use company colors (orange, black, white.)
To begin, we will start with a single sign for hearing protection. Graphic or clip art to portray either ear plugs or ear-muff design. Text to say, "Hearing Protection is a Sound Investment."

Target Market(s)

USA Woodworkers & CNC Machinists - Male, 20-65 years old

Font styles to use
Sans Serif

Colors
f37122

Requirements
Must have
• Client logo
Nice to have
• Use client colors of black, white, & orange

```html
<!DOCTYPE html>
<html lang="en">
<head>
<meta charset="utf-8">
<title>Hearing Protection – Safety Poster</title>
<link rel="stylesheet" href="https://fonts.googleapis.com/css2?family=Montserrat:ital,wght@0,700;0,800;1,600&display=swap">
<style>
  :root {
    --brand-orange: #f37122;
    --ink-black: #111111;
    --paper-white: #ffffff;
    --stage-grey: #4a4a4a;
    --soft-cream: #fde3bf;
  }
  * { margin: 0; padding: 0; box-sizing: border-box; }
  html, body {
    width: 1200px;
    height: 1200px;
    overflow: hidden;
    background: var(--stage-grey);
  }
  .canvas {
    position: relative;
    width: 1200px;
    height: 1200px;
  }
  .poster {
    position: absolute;
    left: 213px;
    top: 94px;
    width: 773px;
    height: 1013px;
    display: block;
  }
  .poster-text { font-family: "Montserrat", sans-serif; }
  .headline-small { font-weight: 800; font-size: 56px; fill: var(--brand-orange); }
  .headline-large { font-weight: 800; font-size: 98px; }
  .ink { fill: var(--ink-black); }
  .paper { fill: var(--paper-white); }
  .brand-name { font-weight: 800; font-size: 42px; fill: var(--ink-black); letter-spacing: 3px; }
  .brand-tagline { font-weight: 600; font-style: italic; font-size: 16px; fill: var(--ink-black); }
</style>
</head>
<body>
<main class="canvas">
  <svg class="poster" viewBox="0 0 773 1013" xmlns="http://www.w3.org/2000/svg">
    <defs>
      <clipPath id="poster-clip"><rect width="773" height="1013"/></clipPath>
      <linearGradient id="graphic-tone" x1="0" y1="0" x2="0" y2="1">
        <stop offset="0" stop-color="#e6e6e6"/>
        <stop offset="1" stop-color="#f7a66a"/>
      </linearGradient>
    </defs>

    <g clip-path="url(#poster-clip)">
      <!-- poster base -->
      <rect class="poster-base" width="773" height="1013" fill="var(--brand-orange)"/>
      <!-- inner frame -->
      <rect class="inner-frame" x="24" y="26" width="725" height="966" fill="none" stroke="var(--paper-white)" stroke-width="6"/>
      <!-- footer brand band -->
      <rect class="brand-band" x="24" y="872" width="725" height="120" fill="var(--paper-white)"/>

      <!-- emblem ring -->
      <circle class="emblem-ring" cx="404" cy="251" r="343" fill="var(--paper-white)" stroke="var(--ink-black)" stroke-width="17"/>
    </g>

    <!-- ear-muff graphic area -->
    <rect class="earmuff-graphic" x="200" y="40" width="396" height="318" rx="28" fill="url(#graphic-tone)"
          role="img" aria-label="Illustration of ear-muff hearing protection with a speaker sound icon between the cups"/>

    <text class="poster-text headline-small" x="404" y="452" text-anchor="middle">HEARING</text>
    <text class="poster-text headline-small" x="404" y="506" text-anchor="middle">PROTECTION</text>

    <!-- check badge -->
    <g class="check-badge">
      <circle cx="404" cy="584" r="54" fill="var(--ink-black)" stroke="var(--paper-white)" stroke-width="8"/>
      <path d="M380 586 L397 603 L429 569" fill="none" stroke="var(--paper-white)" stroke-width="9" stroke-linecap="round" stroke-linejoin="round"/>
    </g>

    <text class="poster-text headline-large" x="404" y="736" text-anchor="middle"><tspan class="ink">IS </tspan><tspan class="paper">A SOUND</tspan></text>
    <text class="poster-text headline-large ink" x="404" y="836" text-anchor="middle">INVESTMENT</text>

    <!-- brand block -->
    <text class="poster-text brand-name" x="386" y="936" text-anchor="middle">GRAINLINE SUPPLY</text>
    <text class="poster-text brand-tagline" x="386" y="966" text-anchor="middle">Your source for industrial cutting tools!</text>
  </svg>
</main>
</body>
</html>
```